business card for author of crime novel

I am an author with a new book. I need a business card with the book's cover on one side (already uploaded), and contact details on the other.

Tom Velasquin
Author

telephone: 917-555-0162
website: www.tomvelasquin.example
facebook: friendpage.example/tvelasquin
twitter: chirpline.example/tvelasquin
email: tvelasquin@mailbox.example

Target Market(s)

Readers of mystery books

Industry/Entity Type

Business

Contact Information for Business Card

Tom Velasquin
Author

telephone: 917-555-0162

Font styles to use
Serif
Sans Serif

Requirements
Must have
• Book cover on one side. My contact info on the other, with the name of the book repeated if that makes sense. Clean design.
Should not have
• Overly ornate, too formal, too distracting

```html
<!DOCTYPE html>
<html lang="en">
<head>
<meta charset="utf-8">
<title>Tom Velasquin – Author Business Card</title>
<link rel="stylesheet" href="https://fonts.googleapis.com/css2?family=Saira+Stencil+One&family=Dosis:wght@400;500&family=Special+Elite&family=Cinzel:wght@400&family=Oswald:wght@400&display=swap">
<style>
  :root {
    --backdrop: #ece7df;
    --card-dark: #2a2622;
    --card-dark-edge: #2c2b27;
    --amber: #d3942b;
    --gold-panel: #c9952f;
    --ink: #121010;
    --white: #f4f1ea;
    --cover-blue-light: #8fa4ad;
    --cover-blue-dark: #2d3c44;
    --cover-name: #f2e53a;
    --paper: #e6cf9f;
    --paper-shade: #caa96d;
  }
  * { box-sizing: border-box; margin: 0; padding: 0; }
  html, body { width: 1200px; height: 1000px; overflow: hidden; }
  body { background: var(--backdrop); position: relative; }

  .card { position: absolute; overflow: hidden; box-shadow: 0 4px 14px rgba(0,0,0,.25); }

  /* Contact side */
  .card--contact {
    left: 180px; top: 30px; width: 455px; height: 690px;
    background: var(--card-dark);
  }
  .contact__backdrop {
    position: absolute; inset: 0;
    background: linear-gradient(160deg, rgba(90,80,68,.35) 0%, rgba(60,54,46,.25) 45%, rgba(42,38,34,0) 80%);
  }
  .contact__name {
    position: absolute; left: 70px; top: 170px;
    font-family: "Saira Stencil One", sans-serif; font-weight: 400;
    font-size: 29px; letter-spacing: 1px; color: var(--amber);
    text-transform: uppercase; white-space: nowrap;
  }
  .contact__role {
    position: absolute; left: 68px; top: 210px;
    font-family: "Dosis", sans-serif; font-weight: 400; font-size: 25px; color: var(--white);
  }
  .contact__list { position: absolute; left: 55px; top: 310px; list-style: none; }
  .contact__item {
    display: flex; align-items: center; height: 37px; white-space: nowrap;
    font-family: "Dosis", sans-serif; font-weight: 400; font-size: 24px; color: var(--amber);
  }
  .contact__icon { width: 18px; height: 18px; margin-right: 20px; flex: none; }

  /* Cover side */
  .card--cover {
    left: 655px; top: 260px; width: 430px; height: 690px;
    background: var(--card-dark-edge);
  }
  .cover__panel {
    position: absolute; left: 30px; top: 32px; width: 370px; height: 628px;
    background: var(--gold-panel);
  }
  .cover__title {
    position: absolute; left: 0; right: 0; top: 52px; text-align: center;
    font-family: "Special Elite", serif; font-weight: 400; font-size: 30px; color: var(--ink);
    text-transform: uppercase; letter-spacing: 1px; white-space: nowrap;
  }
  .cover__photo {
    position: absolute; left: 40px; top: 100px; width: 295px; height: 420px;
    background: linear-gradient(135deg, var(--cover-blue-light) 0%, #5f7680 45%, var(--cover-blue-dark) 100%);
  }
  .cover__author {
    position: absolute; right: 12px; bottom: 14px; text-align: right;
    font-family: "Cinzel", serif; font-weight: 400; font-size: 22px; line-height: 1.1; color: var(--cover-name);
  }
  .cover__series {
    position: absolute; left: 70px; top: 538px; width: 272px; height: 46px;
    background: var(--paper); border-bottom: 4px solid var(--paper-shade);
    border-radius: 3px; display: flex; align-items: center; justify-content: center;
    font-family: "Oswald", sans-serif; font-weight: 400; font-size: 22px; color: var(--ink);
    white-space: nowrap;
  }
</style>
</head>
<body>

<section class="card card--contact" aria-label="Contact side">
  <div class="contact__backdrop" role="img" aria-label="Faint photo of a brick tenement with fire escapes"></div>
  <h1 class="contact__name">Tom Velasquin</h1>
  <p class="contact__role">Author</p>
  <ul class="contact__list">
    <li class="contact__item">
      <svg class="contact__icon" viewBox="0 0 18 18"><path d="M2 7c0-3 14-3 14 0v2h-4V7H6v2H2z M5 10h8l2 5H3z" fill="#f4f1ea"/></svg>
      917-555-0162
    </li>
    <li class="contact__item">
      <svg class="contact__icon" viewBox="0 0 18 18" fill="none" stroke="#f4f1ea" stroke-width="1.5"><circle cx="9" cy="9" r="7"/><ellipse cx="9" cy="9" rx="3" ry="7"/><path d="M2 9h14"/></svg>
      www.tomvelasquin.example
    </li>
    <li class="contact__item">
      <svg class="contact__icon" viewBox="0 0 18 18"><rect x="2" y="2" width="14" height="14" fill="#f4f1ea"/></svg>
      friendpage.example/tvelasquin
    </li>
    <li class="contact__item">
      <svg class="contact__icon" viewBox="0 0 18 18"><circle cx="9" cy="9" r="7" fill="#f4f1ea"/></svg>
      chirpline.example/tvelasquin
    </li>
    <li class="contact__item">
      <svg class="contact__icon" viewBox="0 0 18 18" fill="none" stroke="#f4f1ea" stroke-width="1.5"><rect x="2" y="4" width="14" height="10"/><path d="M2 4l7 6 7-6"/></svg>
      tvelasquin@mailbox.example
    </li>
  </ul>
</section>

<section class="card card--cover" aria-label="Book cover side">
  <div class="cover__panel">
    <h2 class="cover__title">Dead End Static</h2>
    <div class="cover__photo" role="img" aria-label="Blue-toned photo of a corner tenement building with fire escapes">
      <p class="cover__author">TOM<br>VELASQUIN</p>
    </div>
    <p class="cover__series">A Marlow Keene Mystery</p>
  </div>
</section>

</body>
</html>
```